Website Design for StratoCloud As a Service

We are building a service to allow customers to own their own private clouds easily and cheaply. Owning your own private cloud saves costs, and offers more flexibility than a public cloud provider but has historically been a complex and expensive option.

We plan to offer a service where we build and maintain your own private cloud on your own hardware for a cheap monthly costs. Similar to this service - https://stackorra.com/solutions/private-cloud

We already have a logo and branding in place - we'd like a website design to be tailored from this branding, see attached logo design.

Feel free to add important elements on the home page such as testimonials, client/partner logos, contact form, social media, etc using placeholder contents in addition to the document we attached.

We also plan to add sub-pages in the future so please make sure that your website design has a full navigation menu.

An example of the site we like: https://www.verimoxa.com/ we'd be happy for you to take inspiration from this website.

Target Market(s)

B2B focused, we are targeting start-up/small/medium sized companies who needs help with their cloud and IT infrastructure.

Industry/Entity Type

IT

Number of Pages Required

1 page

Font styles to use
Other font styles liked:
• Please refer to the attachment - font must have Mayeka Demi Bold & Retroica

Requirements
Must have
• Please add placeholder menu since we're planning to have subpages later on.

```html
<!DOCTYPE html>
<html lang="en">
<head>
<meta charset="utf-8">
<title>StratoCloud As a Service</title>
<link href="https://fonts.googleapis.com/css2?family=Nunito:wght@700;800;900&family=Raleway:wght@300;400;500&display=swap" rel="stylesheet">
<style>
:root{
  --blue:#29a9e0;
  --blue-deep:#1f9ad3;
  --ink:#111111;
  --text:#333333;
  --muted:#8a8a8a;
  --panel:#f7f7f7;
  --line:#e3e3e3;
  --white:#ffffff;
  --black:#000000;
  --head:"Nunito",sans-serif;
  --body:"Raleway",sans-serif;
}
*{box-sizing:border-box;margin:0;padding:0}
html,body{width:1200px;height:3221px;overflow:hidden}
body{font-family:var(--body);color:var(--text);background:var(--white);position:relative}
.wrap{position:absolute;left:0;width:1200px}
h2{font-family:var(--head);font-weight:800;color:var(--blue);font-size:40px;line-height:1}

/* hero */
.hero{top:0;height:615px;background:var(--blue);color:var(--white)}
.hero-pattern{position:absolute;inset:0;background:radial-gradient(ellipse at 75% 35%,#3bb3e6 0%,var(--blue) 60%)}
.brand{position:absolute;left:14px;top:16px;display:flex;align-items:center;gap:8px;font-family:var(--head);font-weight:800;font-size:22px;color:var(--white)}
.brand-dot{width:20px;height:20px;border-radius:50%;background:var(--white)}
.nav{position:absolute;right:24px;top:16px;display:flex;gap:17px;font-size:11px}
.nav a{color:var(--white);text-decoration:none}
.hero h1{position:absolute;left:19px;top:136px;width:560px;font-family:var(--head);font-weight:800;font-size:47px;line-height:44px}
.hero-lead{position:absolute;left:19px;top:360px;width:500px;font-weight:300;font-size:20px;line-height:27px}
.btn{display:inline-block;border:1px solid currentColor;font-size:14px;padding:10px 13px;text-transform:uppercase;color:var(--blue);text-decoration:none;background:transparent}
.hero .btn{position:absolute;left:18px;top:478px;color:var(--white);border-color:rgba(255,255,255,.7)}
.scroll-bar{position:absolute;left:0;top:556px;width:394px;height:59px;background:#111;display:flex;align-items:center;font-size:14px}
.scroll-bar span{padding-left:18px;flex:1}
.scroll-arrow{width:59px;height:59px;background:#000;display:flex;align-items:center;justify-content:center}

/* benefits */
.benefits{top:615px;height:583px;background:var(--panel);border:1px solid var(--line)}
.benefits h2{position:absolute;left:19px;top:26px}
.sub{font-size:14px;color:var(--text)}
.benefits .sub{position:absolute;left:19px;top:65px}
.card{position:absolute;width:276px;background:var(--white);border:1px solid var(--line);padding:14px 10px}
.card::before{content:"";display:block;width:40px;height:1px;background:var(--line);margin-bottom:14px}
.card svg{display:block;margin:0 0 40px 2px}
.card h3{font-family:var(--head);font-weight:800;font-size:15px;color:var(--blue);margin-bottom:10px;line-height:17px}
.card p{font-size:14px;line-height:18px}

/* transformation */
.transform{top:1198px;height:624px;background:var(--white)}
.transform h2{position:absolute;left:19px;top:38px}
.transform .intro{position:absolute;left:19px;top:77px;width:1165px;font-size:14px;line-height:18px}
.transform .intro p{margin-bottom:18px}
.tabs{position:absolute;left:19px;top:210px;width:1162px;height:40px;border-bottom:3px solid var(--line);display:flex;font-size:14px;color:var(--muted);text-transform:uppercase}
.tabs li{list-style:none;text-align:center;width:276px;padding-top:2px}
.tabs .active{color:var(--blue);border-bottom:3px solid var(--blue);margin-bottom:-3px;position:relative}
.tabs .active::after{content:"";position:absolute;left:50%;bottom:-12px;margin-left:-9px;border:9px solid transparent;border-top-color:var(--blue);border-bottom:0}
.tab-art{position:absolute;left:19px;top:285px;width:473px;height:300px;background:linear-gradient(135deg,#2aaae1,#1f9ad3)}
.tab-body{position:absolute;left:511px;top:280px;width:660px}
.tab-body h3{font-family:var(--head);font-weight:800;font-size:29px;color:var(--ink);margin-bottom:12px}
.tab-body p{font-size:9.5px;line-height:15px;color:var(--text);margin-bottom:14px}
.tab-body .btn{margin-top:8px}

/* public cloud */
.public{top:1822px;height:400px;background:var(--panel);border-top:1px solid var(--line)}
.public h2{position:absolute;left:19px;top:40px}
.col{position:absolute;top:114px;width:375px}
.col h3{font-family:var(--head);font-weight:800;font-size:21px;line-height:30px;color:var(--ink);margin-bottom:16px}
.col p{font-size:14px;line-height:22.5px}
.public .btn{position:absolute;left:18px;top:333px;padding:10px 22px}

/* difference */
.difference{top:2222px;height:513px;background:var(--black);color:var(--white)}
.difference h2{position:absolute;left:19px;top:26px;color:var(--white);font-size:39px}
.step{position:absolute;width:180px}
.step b{display:block;font-family:var(--head);font-weight:900;font-size:92px;line-height:1;color:#c9c9c9;letter-spacing:-2px}
.step.first b{color:var(--blue)}
.step p{font-size:14px;line-height:18px;margin-top:6px}

/* contact */
.contact{top:2735px;height:486px;background:var(--white)}
.contact h2{position:absolute;left:19px;top:30px}
.form{position:absolute;left:19px;top:83px;width:768px;height:368px;border:1px solid var(--line);padding:20px 13px}
.form h3{font-family:var(--head);font-weight:800;font-size:15px;color:var(--blue);margin-bottom:14px}
.field{position:absolute;border:1px solid var(--line);background:var(--white)}
.form .btn{position:absolute;right:14px;top:315px;padding:10px 22px}
.company{position:absolute;right:21px;top:94px;text-align:right;font-size:14px;line-height:18px;color:var(--ink)}
.company h3{font-family:var(--head);font-weight:800;font-size:15px;color:var(--blue);margin-bottom:12px}
.company strong{font-family:var(--head);font-weight:800;display:block;margin-bottom:18px}
.company p{margin-bottom:18px}
</style>
</head>
<body>

<header class="wrap hero">
  <div class="hero-pattern" role="img" aria-label="Light contour line pattern across the blue background"></div>
  <div class="brand"><span class="brand-dot"></span>StratoCloud</div>
  <nav class="nav"><a href="#">Home</a><a href="#">About Us</a><a href="#">Services</a><a href="#">Pricing</a><a href="#">Contact Us</a></nav>
  <h1>A groundbreaking way for your small business to benefit from the power of the cloud</h1>
  <p class="hero-lead">StratoCloud as a Service is here to help small businesses utilise the power of the cloud without complicated set-ups or scary price tags.</p>
  <a class="btn" href="#">Contact Us</a>
  <div class="scroll-bar"><span>SCROLL DOWN FOR MORE INFORMATION</span>
    <div class="scroll-arrow"><svg width="14" height="18" viewBox="0 0 14 18"><path d="M7 0v16M1 10l6 6 6-6" stroke="#fff" fill="none" stroke-width="1.3"/></svg></div>
  </div>
</header>

<section class="wrap benefits">
  <h2>The SCAAS benefits your business</h2>
  <p class="sub">Find out how SCAAS can help you modernise your infrastructure with a fully managed private cloud</p>

  <div class="card" style="left:18px;top:117px;height:186px">
    <svg width="36" height="40" viewBox="0 0 36 40"><path d="M10 30c-6-6 4-12 8-8s-4 12 4 14M26 10c6 6-4 12-8 8" stroke="#111" stroke-width="5" fill="none" stroke-linecap="round"/></svg>
    <h3>Totally flexible</h3><p>Get the cloud you want and the latest innovations you need</p>
  </div>
  <div class="card" style="left:315px;top:117px;height:186px">
    <svg width="42" height="40" viewBox="0 0 42 40"><ellipse cx="13" cy="8" rx="10" ry="5" fill="#111"/><ellipse cx="13" cy="18" rx="10" ry="5" fill="#111"/><circle cx="28" cy="26" r="11" fill="#111"/></svg>
    <h3>Greater value for money</h3><p>Totally transparent pricing for no nasty month-end surprises</p>
  </div>
  <div class="card" style="left:608px;top:117px;height:186px">
    <svg width="42" height="40" viewBox="0 0 42 40"><path d="M4 6l12 14-12 14h8l12-14-12-14zM20 6l12 14-12 14h8l12-14-12-14z" fill="#111"/></svg>
    <h3>Faster</h3><p>Our private cloud solutions outpace public clouds</p>
  </div>
  <div class="card" style="left:903px;top:117px;height:186px">
    <svg width="42" height="40" viewBox="0 0 42 40"><rect x="4" y="24" width="5" height="14" fill="#111"/><rect x="12" y="16" width="5" height="22" fill="#111"/><circle cx="29" cy="26" r="10" fill="#111"/><path d="M14 12l8-9 8 9" stroke="#111" stroke-width="3" fill="none"/></svg>
    <h3>No consultancy fees</h3><p>We will work with you and charge set fees for everything</p>
  </div>
  <div class="card" style="left:18px;top:328px;height:210px">
    <svg width="42" height="40" viewBox="0 0 42 40"><circle cx="21" cy="20" r="17" stroke="#111" stroke-width="3" fill="none"/><path d="M10 26c0-6 4-8 8-7 2-5 10-5 12 1 4 0 5 6 0 6z" fill="#111"/></svg>
    <h3>Management, monitoring and maintainence</h3><p>They are all included in your monthly price</p>
  </div>
  <div class="card" style="left:315px;top:328px;height:210px">
    <svg width="42" height="40" viewBox="0 0 42 40"><path d="M8 22c-5 0-5-9 1-9 1-9 14-10 16-2 6-1 9 11 1 11z" fill="#111"/><path d="M14 24v10M20 24v12M26 24v10" stroke="#111" stroke-width="2"/></svg>
    <h3>Tried and tested cloud solutions</h3><p>We will deploy the right OpenStratum solutions for your business</p>
  </div>
</section>

<section class="wrap transform">
  <h2>SCAAS can drive your digital transformation today</h2>
  <div class="intro">
    <p style="margin-bottom:18px">Organisation of all shapes and sizes are reaping the time and money saving benefits the cloud brings</p>
    <p>But for small businesses seeking to transition, managing the time and financial costs of transitioning, and knowing whether to opt for a public or private cloud can cause you to hit the pause button. SCAAS is here to help you switch on your cloud transformation in a way that works best for you.</p>
    <p>We deliver and support fully managed private cloud solutions that are:</p>
  </div>
  <ul class="tabs">
    <li class="active">Totally flexible</li><li style="width:300px">Easy</li><li style="width:300px">Powerful</li><li style="width:286px">Scalable</li>
  </ul>
  <div class="tab-art" role="img" aria-label="Isometric illustration of servers, computers, a database and devices on blue"></div>
  <div class="tab-body">
    <h3>Totally Flexible</h3>
    <p>Lorem ipsum dolor sit amet, consectetur adipiscing elit. Phasellus ultricies facilisis lacinia. Praesent lacus est, sollicitudin ut lectus nec, dignissim tincidunt arcu. Aliquam erat volutpat. Morbi in molestie lacus, eleifend lobortis libero. Suspendisse varius ligula vitae lacus pharetra rhoncus. Nunc id euismod arcu. Curabitur tempus augue nec congue elementum. Etiam ac dignissim felis. In eget justo accumsan, efficitur erat eget, aliquet lacus. Etiam lobortis quis nibh vel ullamcorper. Integer suscipit dictum velit non porta. Vestibulum porta ullamcorper risus.</p>
    <p>Lorem ipsum dolor sit amet, consectetur adipiscing elit. Phasellus ultricies facilisis lacinia. Praesent lacus est, sollicitudin ut lectus nec, dignissim tincidunt arcu. Aliquam erat volutpat. Morbi in molestie lacus, eleifend lobortis libero. Suspendisse varius ligula vitae lacus pharetra rhoncus. Nunc id euismod arcu. Curabitur tempus augue nec congue elementum. Etiam ac dignissim felis. In eget justo accumsan, efficitur erat eget, aliquet lacus. Etiam lobortis quis nibh vel ullamcorper. Integer suscipit dictum velit non porta. Vestibulum porta ullamcorper risus.</p>
    <a class="btn" href="#" style="margin-top:20px">Get Started</a>
  </div>
</section>

<section class="wrap public">
  <h2>If you’re using a public cloud now…</h2>
  <div class="col" style="left:19px"><h3>You could be paying too much</h3><p>Public cloud pricing structures have a habit of sneakily scaling up very quickly. With SCAAS, you’ll always know what you’re paying for your private cloud services.</p></div>
  <div class="col" style="left:413px"><h3>You are likely not getting the benefits of full functionality</h3><p>Public cloud providers cannot adopt new innovations and functions as quickly and easily as the private cloud solutions you’ll get from SCAAS.</p></div>
  <div class="col" style="left:807px"><h3>You will be tied to the services your provider can provide</h3><p>Public cloud providers will have a limited suite of products and services to offer you. A SCAAS private cloud has no such limitations</p></div>
  <a class="btn" href="#">Lets Talk</a>
</section>

<section class="wrap difference">
  <h2>The SCAAS Difference</h2>
  <div class="step first" style="left:19px;top:95px"><b>01</b><p>We’ll quickly get to grips with what your organisation needs, and deliver it via our private cloud solutions.</p></div>
  <div class="step" style="left:216px;top:95px"><b>02</b><p>Enjoy the ease of the public cloud, combined with the features, innovations and flexibility of the private cloud.</p></div>
  <div class="step" style="left:413px;top:95px"><b>03</b><p>You can focus on your core business while we support you with a dedicated cloud infrastructure.</p></div>
  <div class="step" style="left:610px;top:95px"><b>04</b><p>We’ll create and deliver the launchpad that will take your business forward.</p></div>
  <div class="step" style="left:807px;top:95px"><b>05</b><p>Get the benefits of your own cloud infrastructure and reduce your operational costs.</p></div>
  <div class="step" style="left:1004px;top:95px"><b>06</b><p>Fast and easy computing, storage and network resources.</p></div>
  <div class="step" style="left:19px;top:328px"><b>07</b><p style="padding-left:8px">Managed operations from private OpenStratum clouds and Kontainera.</p></div>
  <div class="step" style="left:216px;top:328px"><b>08</b><p style="padding-left:8px">We’ll support your growth and scale your cloud as you need it.</p></div>
</section>

<section class="wrap contact">
  <h2>Contact Us</h2>
  <form class="form">
    <h3>Fill in this form</h3>
    <p class="sub">Get the cloud you want and the latest innovations you need</p>
    <div class="field" style="left:12px;top:115px;width:352px;height:38px"></div>
    <div class="field" style="left:388px;top:115px;width:366px;height:38px"></div>
    <div class="field" style="left:12px;top:170px;width:742px;height:115px"></div>
    <a class="btn" href="#">Lets Talk</a>
  </form>
  <div class="company">
    <h3>Company Details</h3>
    <strong>StratoCloud As a Service</strong>
    <p>Address Line 1<br>Address Line 2<br>Address Line 3</p>
    <p>Tel: +1 (123) 456 789<br>Email: address@domain.com</p>
  </div>
</section>

</body>
</html>
```